Square graphic for social media post

I want to create a 1080 x 1080px all-black image for the quote below that I can share on social media. I want the emphasis to be primarily on the quote, secondarily on the portrait, and third (smallest) on the logo. I want the background on the portrait to be edited so it's transparent and just shows the face of the person on a black background (no brick wall visible).

Graphic color: black
Text color: white
Content: "What we went through is going to make the greatest generation of hoteliers our industry has ever seen." << biggest text
Dorian Welk << smaller text
President, Marrowgate Hotels << smaller text
[image of person - use whichever version looks better to you]
[Add Lodging Ledger logo - whichever looks better to you]

This image needs to be readable when sized down much smaller (400x400?) so want the text and portrait to take up most of the space.

I'd like the output both as PNG and original file (preferably Canva). Thanks!

Target Market(s)

Hotel managers

Industry/Entity Type

Hospitality

Font styles to use
Sans Serif

Colors

Designer to choose colors to be used in the design.

Requirements
Must have
• Needs to focus on the quote and the person quoted (the portrait)

```html
<!DOCTYPE html>
<html lang="en">
<head>
<meta charset="utf-8">
<title>Quote Card – Dorian Welk</title>
<link href="https://fonts.googleapis.com/css2?family=Bebas+Neue&family=Montserrat:wght@500;700;800&display=swap" rel="stylesheet">
<style>
  :root {
    --ink: #050505;
    --ink-soft: #111111;
    --paper: #ffffff;
    --band: #3a3a3a;
    --label-text: #1c1c1c;
    --portrait-light: #8c8c8c;
    --portrait-dark: #2a2a2a;
  }
  html, body {
    margin: 0;
    padding: 0;
    width: 1200px;
    height: 1200px;
    overflow: hidden;
    background: var(--ink);
  }
  .quote-card {
    position: relative;
    width: 1200px;
    height: 1200px;
    background: radial-gradient(ellipse at 30% 20%, var(--ink-soft), var(--ink) 70%);
    overflow: hidden;
  }
  .quote-card__art {
    position: absolute;
    inset: 0;
  }
  .quote-text--geo {
    font-family: "Montserrat", sans-serif;
    font-weight: 800;
    fill: var(--paper);
  }
  .quote-text--condensed {
    font-family: "Bebas Neue", "Oswald", sans-serif;
    fill: var(--paper);
  }
  .quote-text--label {
    font-family: "Montserrat", sans-serif;
    font-weight: 800;
    fill: var(--label-text);
  }
  .speaker-name {
    font-family: "Montserrat", sans-serif;
    font-weight: 800;
    fill: var(--paper);
  }
  .speaker-role {
    font-family: "Montserrat", sans-serif;
    font-weight: 500;
    fill: var(--paper);
  }
  .brand-name {
    font-family: "Montserrat", sans-serif;
    font-weight: 700;
    fill: var(--paper);
    letter-spacing: 5px;
  }
  .portrait {
    position: absolute;
    left: 790px;
    top: 775px;
    width: 410px;
    height: 425px;
    background:
      radial-gradient(ellipse 38% 42% at 52% 38%, var(--portrait-light), transparent 75%),
      radial-gradient(ellipse 70% 45% at 55% 100%, var(--portrait-dark), transparent 80%);
  }
</style>
</head>
<body>
<main class="quote-card">
  <svg class="quote-card__art" width="1200" height="1200" viewBox="0 0 1200 1200" xmlns="http://www.w3.org/2000/svg">
    <defs>
      <linearGradient id="nameBand" x1="0" y1="0" x2="1" y2="0">
        <stop offset="0" stop-color="#3a3a3a" stop-opacity="0"/>
        <stop offset="0.45" stop-color="#3a3a3a" stop-opacity="0.9"/>
        <stop offset="1" stop-color="#3a3a3a"/>
      </linearGradient>
    </defs>

    <!-- quote frame with gap for opening mark -->
    <path class="quote-frame" d="M156 150 H77 V927 H1124 V150 H337" fill="none" stroke="#ffffff" stroke-width="2.5"/>

    <!-- opening quotation mark -->
    <g class="quote-mark" fill="#ffffff">
      <path d="M172 192 V128 C172 102 186 86 222 80 L236 78 L240 100 C216 106 208 116 208 132 H236 V192 Z"/>
      <path d="M256 192 V128 C256 102 270 86 306 80 L320 78 L324 100 C300 106 292 116 292 132 H320 V192 Z"/>
    </g>

    <!-- quote -->
    <text class="quote-text--geo" x="175" y="300" font-size="88">WHAT WE</text>
    <text class="quote-text--geo" x="175" y="398" font-size="88" textLength="825" lengthAdjust="spacingAndGlyphs">WENT THROUGH IS</text>
    <text class="quote-text--geo" x="175" y="504" font-size="88" textLength="825" lengthAdjust="spacingAndGlyphs">GOING TO MAKE</text>
    <text class="quote-text--condensed" x="172" y="655" font-size="166" textLength="828" lengthAdjust="spacingAndGlyphs">THE GREATEST</text>
    <text class="quote-text--condensed" x="172" y="775" font-size="96" textLength="830" lengthAdjust="spacingAndGlyphs">GENERATION OF HOTELIERS</text>

    <rect class="quote-label" x="172" y="806" width="760" height="67" fill="#ffffff"/>
    <text class="quote-text--label" x="186" y="856" font-size="44" textLength="578" lengthAdjust="spacingAndGlyphs">OUR INDUSTRY HAS EVER SEEN</text>

    <!-- speaker band -->
    <rect class="speaker-band" x="335" y="986" width="600" height="74" fill="url(#nameBand)"/>
    <text class="speaker-name" x="850" y="1045" font-size="60" text-anchor="end">DORIAN WELK</text>
    <text class="speaker-role" x="845" y="1109" font-size="28" text-anchor="end">President, Marrowgate Hotels</text>

    <!-- publisher name -->
    <g class="brand">
      <circle cx="207" cy="978" r="5" fill="#ffffff"/>
      <text class="brand-name" x="207" y="1030" font-size="26" text-anchor="middle">LODGING</text>
      <text class="brand-name" x="207" y="1068" font-size="26" text-anchor="middle">LEDGER</text>
    </g>
  </svg>

  <div class="portrait" role="img" aria-label="Black-and-white head-and-shoulders portrait of Dorian Welk, smiling, in a dark blazer and white open-collar shirt, on a black background"></div>
</main>
</body>
</html>
```